We need an eye catching logo design and Business Card that portrays our business, which is the cleaning and protecting of stainless steel with an organic non chemical product. This can be separate to the company name or can incorporate it. Maybe even just the company name itself. Company Name is Gleamwise Gleamwise.
Ideal for products exposed to weather elements, ie: balustrading, enclosures, BBQs, we also supply the product so you can do it yourself (DIY).
In addition we would want to include on this card:
1. My Name (Paul Dremmick)
2. Mobile No. (TBA Later)
3. Email address (TBA Later)
4. Web address (TBA Later)
Updates

Please note that we also need suggestions on a logo, as this we do not have this either.

Please note we have update our brief to be more specific.

Thank You.

Paul

Reason: Awaiting for a couple of revised submissions from feedback given.

Target Market(s)

Purchasing officers and government people.

Industry/Entity Type

Steel

Colors

Designer to choose colors to be used in the design.

Requirements
Must have
• 1. Name (Paul Dremmick)
2. Mobile No. (TBA Later)
Should not have
• Should not be to busy looking

```html
<!DOCTYPE html>
<html lang="en">
<head>
<meta charset="utf-8">
<title>Gleamwise Gleamwise – Business Card</title>
<link rel="stylesheet" href="https://fonts.googleapis.com/css2?family=Open+Sans:wght@400;600;700;800&display=swap">
<style>
  :root {
    --page-bg: #ebe8e3;
    --charcoal: #363636;
    --lime: #afca1e;
    --white: #ffffff;
    --ink: #2d2d2d;
    --dash: #9a9a9a;
  }
  html, body {
    margin: 0;
    padding: 0;
    width: 1200px;
    height: 1000px;
    overflow: hidden;
    background: var(--page-bg);
    font-family: "Open Sans", sans-serif;
  }
  .canvas { position: relative; width: 1200px; height: 1000px; }

  .card {
    position: absolute;
    width: 678px;
    height: 407px;
    box-shadow: 0 4px 14px rgba(0,0,0,0.25);
    overflow: hidden;
  }

  /* Front */
  .card-front { left: 262px; top: 75px; background: var(--charcoal); }
  .card-front .band {
    position: absolute; left: 0; right: 0; top: 178px; height: 50px;
    background: var(--white);
  }
  .card-front .trim-line {
    position: absolute; left: 22px; top: 22px; width: 634px; height: 361px;
    border: 1px dashed var(--dash); box-sizing: border-box;
  }
  .card-front .wordmark {
    position: absolute; left: 0; right: 0; top: 118px;
    text-align: center; color: var(--lime);
    font-weight: 800; font-size: 64px; line-height: 82px; letter-spacing: 1px;
  }
  .card-front .wordmark span {
    display: inline-block; background: var(--charcoal); padding: 0 24px;
  }

  /* Back */
  .card-back { left: 260px; top: 518px; background: var(--white); }
  .card-back .top-zone { position: absolute; left: 0; right: 0; top: 0; height: 157px; }
  .card-back .wordmark {
    position: absolute; left: 78px; top: 52px;
    color: var(--lime); font-weight: 800; font-size: 25px; line-height: 28px;
  }
  .card-back .tagline {
    position: absolute; right: 61px; top: 96px;
    color: var(--ink); font-size: 14px; letter-spacing: 0.3px;
  }
  .card-back .info-zone {
    position: absolute; left: 0; right: 0; top: 157px; height: 193px;
    background: var(--charcoal);
  }
  .contact-list { position: absolute; left: 55px; top: 34px; margin: 0; padding: 0; list-style: none; }
  .contact-item {
    display: flex; align-items: center; gap: 8px;
    color: var(--white); font-size: 14.5px; line-height: 18px;
    margin-bottom: 9px;
  }
  .contact-item svg { width: 32px; height: 32px; flex: none; }
  .person { position: absolute; right: 61px; top: 66px; text-align: right; }
  .person-name { color: var(--white); font-size: 25px; letter-spacing: 0.5px; margin: 0; font-weight: 400; }
  .person-role { color: var(--lime); font-size: 15px; letter-spacing: 1px; margin: 4px 0 0; }
  .card-back .web-bar {
    position: absolute; left: 0; right: 0; top: 356px; height: 51px;
    background: var(--lime); color: var(--ink);
    font-size: 21px; text-align: center; line-height: 51px;
  }
</style>
</head>
<body>
<div class="canvas">

  <section class="card card-front" aria-label="Business card front">
    <div class="band"></div>
    <div class="trim-line"></div>
    <div class="wordmark"><span>GLEAMWISE<br>GLEAMWISE</span></div>
  </section>

  <section class="card card-back" aria-label="Business card back">
    <div class="top-zone">
      <div class="wordmark">GLEAMWISE<br>GLEAMWISE</div>
      <div class="tagline">NATURAL CLEANERS FOR STAINLESS STEEL</div>
    </div>
    <div class="info-zone">
      <ul class="contact-list">
        <li class="contact-item">
          <svg viewBox="0 0 32 32" aria-hidden="true"><path fill="#fff" d="M3 9c0-3 5-4 13-4s13 1 13 4v3h-6V9.5c-2-.6-4.5-.8-7-.8s-5 .2-7 .8V12H3z"/><rect x="7" y="13" width="18" height="14" rx="2" fill="#fff"/><g fill="#363636"><circle cx="12" cy="17" r="1.2"/><circle cx="16" cy="17" r="1.2"/><circle cx="20" cy="17" r="1.2"/><circle cx="12" cy="21" r="1.2"/><circle cx="16" cy="21" r="1.2"/><circle cx="20" cy="21" r="1.2"/></g></svg>
          <span>+000 555 0100<br>+000 555 0100</span>
        </li>
        <li class="contact-item">
          <svg viewBox="0 0 32 32" aria-hidden="true"><g fill="none" stroke="#fff" stroke-width="2"><circle cx="16" cy="16" r="13"/><ellipse cx="16" cy="16" rx="6" ry="13"/><path d="M3 16h26M5 9h22M5 23h22M16 3v26"/></g></svg>
          <span>info@gleamwise.com<br>gleamwise.com</span>
        </li>
        <li class="contact-item">
          <svg viewBox="0 0 32 32" aria-hidden="true"><path fill="#fff" d="M16 4 2 17l2 2 2-1.8V29h8v-7h4v7h8V17.2l2 1.8 2-2z"/></svg>
          <span>18 Harbour Lane<br>Portmore 20410</span>
        </li>
      </ul>
      <div class="person">
        <h1 class="person-name">PAUL DREMMICK</h1>
        <p class="person-role">Managing Director</p>
      </div>
    </div>
    <div class="web-bar">gleamwise.com</div>
  </section>

</div>
</body>
</html>
```